Startup photo studio needs full suite design (logo, business cards, etc) starting with a website.

We need a website designed for a startup photo studio in the Sacramento area called Silver Lantern Photo Studio. We do portrait work, specializing in the male form and are looking to get into editorial. We would also like to be able to sell prints, posters and canvasses of our work. I would like an elegant but fun design. One of the most important things a portrait photographer needs is the trust of the model. The website would convey honesty, friendliness and warmth as well. I have a domain name with NetHarbor, silverlanternstudio.example email address should be my name with that domain.

Target Market(s)

Art enthusiasts, business portraits, online dating photos

Industry/Entity Type

Professional Photography

Contact Information for Business Card

Simple please. Just logo and contact info. Phone, email, website. no address required

Logo Text

Silver Lantern Photo Studio --- light tells the story

Number of Pages Required

3 page

Font styles to use
Sans Serif

Colors

Designer to choose colors to be used in the design.

Requirements
Must have
• Simple clean design.
Nice to have
• Somehow one of my photos in the design? maybe not...
Should not have
• No weddings!

```html
<!DOCTYPE html>
<html lang="en">
<head>
<meta charset="utf-8">
<title>Contact — Silver Lantern Photo Studio</title>
<link rel="stylesheet" href="https://fonts.googleapis.com/css2?family=Jost:wght@200;300;400;500&display=swap">
<style>
  :root {
    --ink: #000000;
    --paper: #ffffff;
    --title-grey: #3c3c3c;
    --ghost-grey: #2e2e2e;
    --field-grey: #787878;
    --field-text: #262626;
    --frame-grey: #8a8a8a;
    --nav-line: #9a9a9a;
    --nav-text: #3a3a3a;
  }
  * { box-sizing: border-box; margin: 0; padding: 0; }
  html, body { width: 1200px; height: 672px; overflow: hidden; background: var(--paper); }
  body { position: relative; font-family: "Jost", sans-serif; }

  .contact-section { position: absolute; left: 0; top: 0; width: 1200px; height: 507px; background: var(--ink); }
  .section-title {
    position: absolute; left: 0; width: 1200px; top: 58px; text-align: center;
    font-weight: 200; font-size: 52px; letter-spacing: 3px; color: var(--title-grey); line-height: 1;
  }

  .details-frame { position: absolute; left: 134px; top: 163px; width: 457px; height: 263px; border: 1px solid var(--frame-grey); }
  .detail { position: absolute; left: 394px; display: flex; align-items: flex-start; gap: 8px;
    color: var(--paper); font-size: 8.6px; font-weight: 400; letter-spacing: 0.4px; line-height: 11px; }
  .detail svg { width: 10px; height: 10px; flex: none; margin-top: 1px; }
  .detail-address { top: 256px; }
  .detail-phone { top: 293px; }
  .detail-email { top: 318px; }

  .form-heading-ghost { position: absolute; left: 632px; top: 132px; font-size: 30px; font-weight: 300;
    letter-spacing: 1.5px; color: var(--ghost-grey); line-height: 1; white-space: nowrap; }
  .form-heading-tab { position: absolute; left: 611px; top: 173px; width: 50px; height: 12px; border: 1px solid var(--frame-grey); border-bottom: none; }
  .form-heading { position: absolute; left: 618px; top: 178px; font-size: 11px; font-weight: 400;
    letter-spacing: 0.5px; color: var(--paper); line-height: 1; white-space: nowrap; }

  .field { position: absolute; left: 610px; width: 457px; background: var(--field-grey);
    color: var(--field-text); font-size: 8.4px; letter-spacing: 0.4px; padding-left: 12px; }
  .field-name { top: 203px; height: 32px; line-height: 32px; }
  .field-email { top: 241px; height: 31px; line-height: 31px; }
  .field-message { top: 278px; height: 110px; padding-top: 15px; line-height: 1; }

  .send-button { position: absolute; left: 610px; top: 394px; width: 92px; height: 32px; border: 1px solid var(--frame-grey); padding: 3px; }
  .send-button span { display: block; width: 100%; height: 100%; background: var(--field-grey);
    color: var(--ink); font-size: 8.6px; font-weight: 500; letter-spacing: 0.6px; text-align: center; line-height: 24px; }

  .back-to-top { position: absolute; left: 0; width: 1200px; top: 550px; text-align: center;
    font-size: 8.6px; font-weight: 500; letter-spacing: 0.8px; color: var(--ink); }
  .back-to-top svg { display: block; margin: 0 auto 1px; width: 7px; height: 5px; }

  .footer-nav { position: absolute; left: 253px; top: 590px; width: 694px; height: 30px; border: 1px solid var(--nav-line); }
  .nav-item { position: absolute; top: 0; line-height: 28px; transform: translateX(-50%);
    font-size: 9px; font-weight: 400; letter-spacing: 0.6px; color: var(--nav-text); }

  .social-link { position: absolute; top: 637px; transform: translateX(-50%);
    font-size: 8.6px; font-weight: 500; letter-spacing: 0.6px; color: var(--ink); }
</style>
</head>
<body>
  <section class="contact-section">
    <h1 class="section-title">Contact</h1>

    <div class="details-frame"></div>
    <div class="detail detail-address">
      <svg viewBox="0 0 10 10"><path d="M5 0.5a3.2 3.2 0 0 0-3.2 3.2C1.8 6 5 9.5 5 9.5S8.2 6 8.2 3.7A3.2 3.2 0 0 0 5 0.5zm0 4.4a1.2 1.2 0 1 1 0-2.4 1.2 1.2 0 0 1 0 2.4z" fill="#fff"/></svg>
      <span>2718 Alder Row<br>Fair Oaks, CA 95628</span>
    </div>
    <div class="detail detail-phone">
      <svg viewBox="0 0 10 10"><path d="M2.2 0.6l1.6 2-0.9 1.1c0.6 1.3 1.5 2.2 2.8 2.8l1.1-0.9 2 1.6-0.9 1.6C5 8.6 1.4 5 0.6 1.5z" fill="#fff"/></svg>
      <span>555.014.2287</span>
    </div>
    <div class="detail detail-email">
      <svg viewBox="0 0 10 10"><rect x="0.5" y="2" width="9" height="6.2" fill="#fff"/><path d="M0.5 2.2L5 5.4 9.5 2.2" fill="none" stroke="#000" stroke-width="0.8"/></svg>
      <span>hello@silverlanternstudio.example</span>
    </div>

    <div class="form-heading-ghost">send us message</div>
    <div class="form-heading-tab"></div>
    <div class="form-heading">send us message</div>

    <div class="field field-name">name</div>
    <div class="field field-email">email</div>
    <div class="field field-message">message</div>
    <div class="send-button"><span>send</span></div>
  </section>

  <div class="back-to-top">
    <svg viewBox="0 0 7 5"><path d="M0.5 4.2L3.5 1 6.5 4.2" fill="none" stroke="#000" stroke-width="0.8"/></svg>
    back to top
  </div>

  <nav class="footer-nav">
    <span class="nav-item" style="left:109px">Home</span>
    <span class="nav-item" style="left:172px">About</span>
    <span class="nav-item" style="left:242px">Services</span>
    <span class="nav-item" style="left:319px">Portfolio</span>
    <span class="nav-item" style="left:389px">Team</span>
    <span class="nav-item" style="left:446px">Blog</span>
    <span class="nav-item" style="left:507px">Clients</span>
    <span class="nav-item" style="left:579px">Contact</span>
  </nav>

  <span class="social-link" style="left:512px">lumenfeed</span>
  <span class="social-link" style="left:596px">chirpline</span>
  <span class="social-link" style="left:683px">framecast</span>
</body>
</html>
```